Brisk Hollow Builders Needs A Flyer

We need a flyer for our newest product "The Cedarlane Garden Workroom"

Here is some copy for the flyer:

1. More and more people everyday are working from home and finding it difficult to disconnect from home activities in order to focus on their work. They are also finding it very expensive to add on to their existing house for a quiet place. Our archatectually stunning, Cedarlane Garden Workroom is the answer. The office studio measures 16' wide and 10' deep. 160 Square feet of space.

Perfect for dozens of purposes. Home office, design studio, artist studio, home school office, reading room, craft studio, drafting room.

Features include:

- Steel Framing. 40-60% lighter then wood, higher strength to weight ratio, resistant to mold and fire and steel is the most recycled material on earth!
- Spray foam insulation. Cool in the summer and warm in the winter.
- HVAC Mini Split with wireless remote control and thermostat.
- 100% Off grid with enough solar and battery storage to run your entire office. No need to pay for an expensive electric installation.
- Flush fitting floor outlets to reduce wires.
- TV mount (Optional with pre-wired electric, HDMI, digital audio & Cat 6)
- Windows are tempered glass custom made by Morvik Glazing.
- Solar qualifies for a 26% tax credit. This is not a write-off rather it is a direct reduction on your tax obligation.
- Thousands of dollars less than adding onto your home.
- Custom color, siding, features available.

This beautiful back yard office is delivered 100% assembled and ready to enjoy on the day of delivery.

We ship nationwide from our factory in South Carolina. Give us a call anytime to speak to a designer and start your dream office today!

555-318-4027
info@BriskHollowBuilders.example

```html
<!DOCTYPE html>
<html lang="en">
<head>
<meta charset="utf-8">
<title>The Cedarlane Garden Workroom – Brisk Hollow Builders</title>
<link rel="stylesheet" href="https://fonts.googleapis.com/css2?family=Montserrat:wght@600;700;800;900&family=Oswald:wght@500;600;700&family=Roboto:wght@400;500&display=swap">
<style>
  :root {
    --black: #050505;
    --orange: #e39a22;
    --orange-deep: #ee7d1f;
    --flame: #f26a21;
    --yellow: #ffd400;
    --green: #5aa046;
    --green-dark: #3f7f30;
    --cream: #fbf6e4;
    --white: #ffffff;
    --ink: #111111;
  }
  * { box-sizing: border-box; margin: 0; padding: 0; }
  html, body { width: 1015px; height: 1200px; overflow: hidden; background: var(--white); }
  .flyer { position: relative; width: 1015px; height: 1200px; overflow: hidden; background: var(--black); font-family: "Roboto", Arial, sans-serif; }

  /* Hero photos */
  .hero { position: absolute; top: 0; left: 0; width: 1015px; height: 290px; background: var(--white); }
  .hero-photo { position: absolute; top: 0; height: 286px; }
  .hero-photo--studio { left: 0; width: 475px; background: linear-gradient(180deg, #9fc3d9 0%, #7fa167 38%, #3f4a3a 62%, #8a9a6a 100%); }
  .hero-photo--rear { left: 481px; width: 534px; background: linear-gradient(180deg, #b9d3e3 0%, #6f8f52 35%, #3b3c3b 55%, #4a4a48 75%, #7d9456 100%); }
  .brand-box { position: absolute; left: 378px; top: 150px; width: 262px; height: 140px; background: var(--white);
    display: flex; align-items: center; justify-content: center; gap: 10px; }
  .brand-dot { width: 20px; height: 20px; border-radius: 50%; background: var(--green); flex: none; }
  .brand-name { font-family: "Montserrat", sans-serif; font-weight: 800; font-size: 20px; color: var(--green-dark); text-transform: uppercase; line-height: 1.1; }

  /* Title */
  .title { position: absolute; top: 306px; left: 0; width: 1015px; text-align: center; font-family: "Montserrat", sans-serif; font-weight: 900; text-transform: uppercase; line-height: 1.04; letter-spacing: -0.5px; }
  .title-line { display: block; font-size: 58px; }
  .title-line--top { background: linear-gradient(90deg, var(--flame), #f5a623); -webkit-background-clip: text; background-clip: text; color: transparent; }
  .title-line--bottom { color: var(--yellow); }

  /* Purposes band */
  .purposes-band { position: absolute; top: 440px; left: 0; width: 1015px; height: 190px; }
  .purposes-band svg { position: absolute; inset: 0; }
  .framing-art { position: absolute; left: 12px; top: 70px; width: 340px; height: 112px; background: linear-gradient(180deg, rgba(60,35,10,.55), rgba(60,35,10,.35)); }
  .purposes { position: absolute; left: 392px; top: 50px; width: 610px; }
  .purposes-heading { font-family: "Oswald", sans-serif; font-weight: 700; font-size: 32px; color: var(--green); text-transform: uppercase; line-height: 1; }
  .purposes-list { margin-top: 6px; font-family: "Oswald", sans-serif; font-weight: 600; font-size: 21px; color: var(--ink); text-transform: uppercase; line-height: 1.2; }

  /* Body */
  .body { position: absolute; top: 630px; left: 0; width: 1015px; height: 500px; overflow: hidden; background: linear-gradient(180deg, var(--white), var(--cream)); }
  .intro { position: absolute; top: 6px; left: 90px; width: 835px; text-align: center; font-size: 12.5px; line-height: 1.3; color: var(--ink); text-transform: uppercase; }
  .intro-highlight { display: block; color: var(--green); font-family: "Montserrat", sans-serif; font-weight: 800; font-size: 12.5px; margin-top: 3px; }

  .features { position: absolute; top: 100px; left: 60px; width: 550px; }
  .features-heading { display: inline-block; background: var(--green); color: var(--white); font-family: "Montserrat", sans-serif; font-weight: 800; font-size: 20px; text-transform: uppercase; padding: 2px 34px 2px 10px; clip-path: polygon(0 0, 100% 0, 88% 100%, 0 100%); }
  .feature-list { list-style: none; margin-top: 8px; }
  .feature-list li { position: relative; padding-left: 22px; font-size: 13.5px; line-height: 1.3; color: var(--ink); margin-bottom: 6px; }
  .feature-list li::before { content: ""; position: absolute; left: 4px; top: 6px; width: 7px; height: 7px; border-radius: 50%; background: var(--green); }

  .sun { position: absolute; left: 630px; top: 150px; width: 560px; height: 560px; border-radius: 50%; background: radial-gradient(circle at 25% 40%, var(--yellow) 0%, #f7b81b 45%, var(--orange-deep) 80%); }
  .delivery-badge { position: absolute; left: 665px; top: 96px; width: 280px; height: 280px; border-radius: 50%; background: var(--green); display: flex; align-items: center; justify-content: center; text-align: center; padding: 0 44px;
    font-family: "Montserrat", sans-serif; font-weight: 800; font-size: 17px; line-height: 1.25; color: var(--white); text-transform: uppercase; }
  .cta { position: absolute; left: 650px; top: 394px; width: 340px; text-align: center; font-family: "Montserrat", sans-serif; text-transform: uppercase; color: var(--ink); }
  .cta-ship { font-weight: 800; font-size: 12px; line-height: 1.25; }
  .cta-main { font-weight: 800; font-size: 17px; line-height: 1.2; margin-top: 3px; }

  /* Footer */
  .footer { position: absolute; left: 0; top: 1130px; width: 1015px; height: 70px; background: var(--black); display: flex; align-items: center; justify-content: space-between; padding: 0 50px;
    font-family: "Montserrat", sans-serif; font-weight: 700; color: var(--orange); }
  .contact { display: flex; align-items: center; gap: 12px; }
  .contact--email { font-size: 23px; text-transform: uppercase; }
  .contact--phone { font-size: 25px; }
  .contact-icon { width: 28px; height: 28px; flex: none; }
</style>
</head>
<body>
<main class="flyer">

  <header class="hero">
    <div class="hero-photo hero-photo--studio" role="img" aria-label="Photo of a dark modern garden studio with glass doors, furnished interior, set among trees"></div>
    <div class="hero-photo hero-photo--rear" role="img" aria-label="Photo of the rear of the studio with solar panels on its sloped roof, in a landscaped yard"></div>
    <div class="brand-box">
      <span class="brand-dot"></span>
      <span class="brand-name">Brisk Hollow<br>Builders</span>
    </div>
  </header>

  <h1 class="title">
    <span class="title-line title-line--top">The Cedarlane</span>
    <span class="title-line title-line--bottom">Garden Workroom</span>
  </h1>

  <section class="purposes-band">
    <svg width="1015" height="190" viewBox="0 0 1015 190" aria-hidden="true">
      <polygon points="0,110 400,20 1015,55 1015,158 0,190" fill="#e39a22"/>
    </svg>
    <div class="framing-art" role="img" aria-label="Illustration of the steel wall framing of the studio"></div>
    <div class="purposes">
      <h2 class="purposes-heading">Perfect for dozens of purposes</h2>
      <p class="purposes-list">Home office, design studio, artist studio,<br>home school office, reading room,<br>craft studio, drafting room.</p>
    </div>
  </section>

  <section class="body">
    <p class="intro">
      More and more people everyday are working from home and finding it difficult to disconnect from home activities in order to focus on their work. They are also finding it very expensive to add on to their existing house for a quiet place.
      <span class="intro-highlight">Our archatectually stunning, Cedarlane Garden Workroom is the answer.<br>The office studio measures 16' wide and 10' deep. 160 square feet of space.</span>
    </p>

    <div class="sun" aria-hidden="true"></div>

    <div class="features">
      <h2 class="features-heading">Features</h2>
      <ul class="feature-list">
        <li>Steel Framing. 40-60% lighter then wood, higher strength to weight ratio, resistant to mold and fire and steel is the most recycled material on earth!</li>
        <li>Spray foam insulation. Cool in the summer and warm in the winter.</li>
        <li>HVAC Mini Split with wireless remote control and thermostat.</li>
        <li>100% Off grid with enough solar and battery storage to run your entire office. No need to pay for an expensive electric installation.</li>
        <li>Flush fitting floor outlets to reduce wires.</li>
        <li>TV mount (Optional with pre-wired electric, HDMI, digital audio &amp; Cat 6)</li>
        <li>Windows are tempered glass custom made by Morvik Glazing.</li>
        <li>Solar qualifies for a 26% tax credit. This is not a write-off rather it is a direct reduction on your tax obligation.</li>
        <li>Thousands of dollars less than adding onto your home.</li>
        <li>Custom color, siding, features available.</li>
      </ul>
    </div>

    <p class="delivery-badge">This beautiful back yard office is delivered 100% assembled and ready to enjoy on the day of delivery.</p>

    <div class="cta">
      <p class="cta-ship">We ship nationwide from our<br>factory in South Carolina.<br>Give us a call</p>
      <p class="cta-main">Anytime to speak to a designer and start your dream office today!</p>
    </div>
  </section>

  <footer class="footer">
    <div class="contact contact--email">
      <svg class="contact-icon" viewBox="0 0 28 28" aria-hidden="true">
        <circle cx="14" cy="14" r="13" fill="#fff"/>
        <rect x="7" y="9" width="14" height="10" fill="none" stroke="#050505" stroke-width="1.8"/>
        <polyline points="7,9 14,15 21,9" fill="none" stroke="#050505" stroke-width="1.8"/>
      </svg>
      <span>info@BriskHollowBuilders.example</span>
    </div>
    <div class="contact contact--phone">
      <svg class="contact-icon" viewBox="0 0 28 28" aria-hidden="true">
        <circle cx="14" cy="14" r="13" fill="#fff"/>
        <path d="M9 7c1 0 2 2.5 2 3.3s-1.3 1.2-1.1 2c.5 1.8 2 3.3 3.8 3.9.8.2 1.2-1.1 2-1.1s3.3 1 3.3 2-1.5 3-3 2.8C11 19.4 8.6 17 8 12.8 7.8 11 8 7 9 7z" fill="#050505"/>
      </svg>
      <span>555-318-4027</span>
    </div>
  </footer>

</main>
</body>
</html>
```